Android App Design Project

Hi my name is Keril, and I'm an android developer. I'm searching for a professional designer that can design my app.I have already launched the app and you can find it in the appora depot.

Main Requirements
- 15 sport icons
- 6 android pages
- Action bar
- Buttons and other icons

You need to do all requirements to submit a design. I need the design in both JPEG format and Photoshop PSD format. If you are interested then please download the PDF file ,it will help you a lot.
The name of the app is "MATCH VUE Prime" you can find it in Appora Shelf.

NOTICE: You might read that the Payment is not guaranteed if I'm not happy with the design BUT if you make a good design and you win the contest, then you become my main designer that means if I want to change or add something to the design of the app in the future I return to you "the winner" directly to make the redesign and get paid for it.

Regards.
Skype: Idun marvelo "idun47"
E-mail: idunkeril@mailvox.test

Industry/Entity Type

Tv

Requirements
Must have
• - 15 sport icons
- 6 android pages
- Action bar
- Buttons and other icons

```html
<!DOCTYPE html>
<html lang="en">
<head>
<meta charset="utf-8">
<title>Live Scores</title>
<link rel="stylesheet" href="https://fonts.googleapis.com/css2?family=Ubuntu:wght@400;500&display=swap">
<style>
  :root {
    --orange-top: #f6913a;
    --orange-bottom: #e15e12;
    --orange-dark: #c4500e;
    --orange-deep: #a9430b;
    --accent-vs: #ec6a1f;
    --bg-dark: #2a2a2a;
    --bg-darker: #232323;
    --divider-light: #4a4a4a;
    --divider-shadow: #161616;
    --text-light: #f2f2f2;
    --text-dim: #e6e6e6;
    --pill-bg: #2f4158;
    --pill-edge: #5d7492;
    --white: #ffffff;
  }
  * { box-sizing: border-box; margin: 0; padding: 0; }
  html, body { width: 817px; height: 1200px; overflow: hidden; }
  body {
    font-family: "Ubuntu", "Trebuchet MS", sans-serif;
    color: var(--text-light);
    background: var(--bg-dark);
  }
  .app-screen {
    position: relative;
    width: 817px;
    height: 1200px;
    overflow: hidden;
    background:
      repeating-linear-gradient(45deg, rgba(255,255,255,0.018) 0 3px, rgba(0,0,0,0.03) 3px 6px),
      linear-gradient(var(--bg-dark), var(--bg-darker));
  }
  /* Action bar */
  .action-bar {
    position: relative;
    height: 86px;
    background: linear-gradient(var(--orange-top), var(--orange-bottom));
    border-bottom: 2px solid var(--orange-deep);
  }
  .icon-button {
    position: absolute;
    top: 13px;
    width: 78px;
    height: 58px;
    border-radius: 10px;
    background: linear-gradient(#e8752a, var(--orange-dark));
    box-shadow: inset 0 1px 0 rgba(255,255,255,0.35), 0 1px 2px rgba(0,0,0,0.3);
    display: flex;
    align-items: center;
    justify-content: center;
  }
  .icon-button--back { left: 10px; }
  .icon-button--settings { left: 708px; }
  .segmented-tabs {
    position: absolute;
    left: 222px;
    top: 20px;
    width: 378px;
    height: 52px;
    display: flex;
    border-radius: 9px;
    overflow: hidden;
    border: 2px solid var(--orange-deep);
    box-shadow: inset 0 1px 0 rgba(255,255,255,0.3);
  }
  .segmented-tabs__tab {
    flex: 1;
    display: flex;
    align-items: center;
    justify-content: center;
    font-size: 30px;
  }
  .segmented-tabs__tab--latest {
    background: linear-gradient(#fbb06a, #f08a3a);
    color: var(--white);
    border-right: 2px solid var(--orange-deep);
  }
  .segmented-tabs__tab--score {
    background: linear-gradient(#e2651a, #c9530f);
    color: #3a1a05;
  }
  /* Feed */
  .match-title, .match-score {
    border-bottom: 2px solid var(--divider-shadow);
    box-shadow: 0 2px 0 var(--divider-light);
  }
  .match-title {
    padding-left: 36px;
    font-size: 30px;
    line-height: 38px;
    color: var(--text-dim);
  }
  .match-title .vs { color: var(--accent-vs); }
  .match-score {
    position: relative;
    text-align: center;
    font-size: 30px;
    line-height: 34px;
  }
  .match-score__label,
  .match-score__overs {
    position: absolute;
    left: 0; right: 0;
  }
  .match-score__pill {
    position: absolute;
    left: 314px;
    width: 189px;
    height: 51px;
    line-height: 47px;
    border-radius: 9px;
    background: linear-gradient(#3a4f6a, var(--pill-bg));
    border: 2px solid var(--pill-edge);
    color: var(--white);
    font-size: 29px;
  }
  .title-first  { height: 151px; padding-top: 28px; }
  .title-second { height: 166px; padding-top: 19px; }
  .title-third  { height: 186px; padding-top: 29px; }
  .score-first  { height: 210px; }
  .score-second { height: 204px; }
  .score-third  { height: 197px; border-bottom: none; box-shadow: none; }
  .score-first .match-score__label  { top: 17px; }
  .score-first .match-score__pill   { top: 72px; }
  .score-first .match-score__overs  { top: 144px; }
  .score-second .match-score__label { top: 24px; }
  .score-second .match-score__pill  { top: 72px; }
  .score-second .match-score__overs { top: 138px; }
  .score-third .match-score__label  { top: 27px; }
  .score-third .match-score__pill   { top: 77px; }
  .score-third .match-score__overs  { top: 150px; }
</style>
</head>
<body>
<main class="app-screen">
  <header class="action-bar">
    <div class="icon-button icon-button--back" aria-label="Back">
      <svg width="40" height="34" viewBox="0 0 40 34"><path d="M2 17 L18 2 V11 H38 V23 H18 V32 Z" fill="#fff"/></svg>
    </div>
    <nav class="segmented-tabs">
      <div class="segmented-tabs__tab segmented-tabs__tab--latest">Latest</div>
      <div class="segmented-tabs__tab segmented-tabs__tab--score">Score</div>
    </nav>
    <div class="icon-button icon-button--settings" aria-label="Settings">
      <svg width="42" height="42" viewBox="0 0 42 42">
        <g fill="#fff" transform="translate(21 21)">
          <rect x="-4" y="-20" width="8" height="10" rx="1"/>
          <rect x="-4" y="-20" width="8" height="10" rx="1" transform="rotate(45)"/>
          <rect x="-4" y="-20" width="8" height="10" rx="1" transform="rotate(90)"/>
          <rect x="-4" y="-20" width="8" height="10" rx="1" transform="rotate(135)"/>
          <rect x="-4" y="-20" width="8" height="10" rx="1" transform="rotate(180)"/>
          <rect x="-4" y="-20" width="8" height="10" rx="1" transform="rotate(225)"/>
          <rect x="-4" y="-20" width="8" height="10" rx="1" transform="rotate(270)"/>
          <rect x="-4" y="-20" width="8" height="10" rx="1" transform="rotate(315)"/>
          <circle r="14"/>
        </g>
        <circle cx="21" cy="21" r="6" fill="#d85a12"/>
      </svg>
    </div>
  </header>

  <section class="match-title title-first">
    <p>Austrilia <span class="vs">vs</span> India</p>
    <p>Criket matche live score</p>
    <p>From india</p>
  </section>
  <section class="match-score score-first">
    <p class="match-score__label">Matche score</p>
    <p class="match-score__pill">250 / 5</p>
    <p class="match-score__overs">35 overs</p>
  </section>

  <section class="match-title title-second">
    <p>Westindies <span class="vs">vs</span> Pakisthan</p>
    <p>Cricket matche &nbsp;live score</p>
    <p>From pakisthan</p>
  </section>
  <section class="match-score score-second">
    <p class="match-score__label">Matche score</p>
    <p class="match-score__pill">280 / 5</p>
    <p class="match-score__overs">48 overs</p>
  </section>

  <section class="match-title title-third">
    <p>Austrilia <span class="vs">vs</span> India</p>
    <p>Criket matche live score</p>
    <p>From india</p>
  </section>
  <section class="match-score score-third">
    <p class="match-score__label">Matche score</p>
    <p class="match-score__pill">250 / 5</p>
    <p class="match-score__overs">48 overs</p>
  </section>
</main>
</body>
</html>
```